Stationery Design Project

Would like to have the design elements we created in for our website (www.brook-estates.com), incorporated in a stationery design layout.
Updates
Colors used in the logo attachments do not need to be used. We are open to different color variations. Looking for a crisp, clean, modern update using the design elements in attachments and which can also be viewed on or website.
A note to designers:
Project Deadline Extended
Reason: Due to update in our project description and requirements, we have decided to extend the deadline of this project to provide ample opportunity to all designers participating .
Requirements
Must have
- Must have continuity with the theme and design features used in our website. Have attached .jpg images of some of the design elements.

```html
<!DOCTYPE html>
<html lang="en">
<head>
<meta charset="utf-8">
<title>Brook Estates – Letterhead</title>
<link rel="stylesheet" href="https://fonts.googleapis.com/css2?family=Questrial&family=PT+Sans:wght@400;700&display=swap">
<style>
  :root {
    --frame: #000000;
    --paper: #ffffff;
    --ink: #2a2c20;
    --text: #1c1c1c;
    --rule: #8a8a8a;
    --green: #5fb55a;
    --forest: #1f2419;
    --footer-text: #ffffff;
  }
  * { margin: 0; padding: 0; box-sizing: border-box; }
  html, body {
    width: 850px;
    height: 1200px;
    overflow: hidden;
    background: var(--frame);
  }
  .canvas {
    position: relative;
    width: 850px;
    height: 1200px;
    background: var(--frame);
  }
  .sheet {
    position: absolute;
    left: 16px;
    top: 16px;
    width: 818px;
    height: 1168px;
    background: var(--paper);
    overflow: hidden;
  }
  .brand-name {
    position: absolute;
    left: 50px;
    top: 82px;
    font-family: "Questrial", sans-serif;
    font-size: 46px;
    line-height: 1;
    color: var(--ink);
    letter-spacing: -0.5px;
  }
  .contact-rule {
    position: absolute;
    left: 565px;
    top: 48px;
    width: 1px;
    height: 142px;
    background: var(--rule);
  }
  .contact {
    position: absolute;
    left: 583px;
    top: 49px;
    font-family: "PT Sans", sans-serif;
    font-size: 15px;
    line-height: 19.5px;
    color: var(--text);
    font-style: normal;
    letter-spacing: -0.2px;
  }
  .contact .company { font-weight: 700; }
  .contact .email-label { margin-top: 19px; }
  .footer-accent {
    position: absolute;
    left: 0;
    top: 1126px;
    width: 100%;
    height: 14px;
    background: var(--green);
  }
  .footer-bar {
    position: absolute;
    left: 0;
    top: 1140px;
    width: 100%;
    height: 28px;
    background: var(--forest);
    display: flex;
    align-items: center;
    justify-content: center;
  }
  .footer-web {
    font-family: "PT Sans", sans-serif;
    font-size: 15px;
    letter-spacing: 3.2px;
    color: var(--footer-text);
  }
</style>
</head>
<body>
  <div class="canvas">
    <div class="sheet">
      <div class="brand-name">Brook Estates</div>

      <div class="contact-rule"></div>
      <address class="contact">
        <div class="company">Brook Estates, Inc.</div>
        <div>418 Millrace Lane Suite 120</div>
        <div>Alder Falls, GA 30512</div>
        <div>PHONE: (555) 014-2237</div>
        <div>FAX: (555) 014-2290</div>
        <div class="email-label">E-mail us:</div>
        <div>info@brook-estates.com</div>
      </address>

      <div class="footer-accent"></div>
      <div class="footer-bar">
        <span class="footer-web">www.brook-estates.com</span>
      </div>
    </div>
  </div>
</body>
</html>
```